For Lease Sign to Attract National Retail Tenants

Attached is a logo design that was created by Pixel Harbor. I will like to develop a leasing sign that is 4 foot wide by 4 foot high or 4 feet wide and 6 feet high. I would like the sign to have a black background and use the colors that are in the logo. These will be signs that are placed in front of shopping centers and are often read by passing motorist so the sign must be simple, clean, very easy to read, distinctive, and have as few words as possible. It would be good if small amounts of bright green can be added as a boarder or ????? The text should be FOR LEASE, 555-283-7716, Reed Halvorsen. I will want to also design cards and letter head around the same theme.

Target Market(s)

National retail tenants wanting to lease space in my shopping centers

Industry/Entity Type

Real Estate Development

Contact Information for Business Card

Tall Oak RP, LLC Reed Halvorsen President & CEO 4172 Marrow Ave. Suite 305 Fenwick, CA 90000 555-283-7716 reedhalvorsen@mailbox.example

```html
<!DOCTYPE html>
<html lang="en">
<head>
<meta charset="utf-8">
<title>For Lease Sign – Tall Oak RP, LLC</title>
<link rel="stylesheet" href="https://fonts.googleapis.com/css2?family=Montserrat:wght@500;600;800&display=swap">
<style>
  :root {
    --canvas: #ffffff;
    --frame: #9e9e9e;
    --signal-red: #ed1c24;
    --panel: #ffffff;
    --ink-dark: #3d3a3a;
    --headline-ink: #ffffff;
  }
  html, body {
    margin: 0;
    padding: 0;
    width: 1200px;
    height: 1200px;
    overflow: hidden;
    background: var(--canvas);
  }
  .canvas {
    position: relative;
    width: 1200px;
    height: 1200px;
    font-family: "Montserrat", Arial, sans-serif;
  }
  .lease-sign {
    position: absolute;
    left: 303px;
    top: 154px;
    width: 594px;
    height: 893px;
    box-sizing: border-box;
    border: 16px solid var(--frame);
    background: var(--panel);
  }
  .headline-band {
    position: absolute;
    left: 0;
    top: 0;
    width: 100%;
    height: 430px;
    background: var(--signal-red);
  }
  .headline {
    position: absolute;
    left: 0;
    width: 100%;
    margin: 0;
    text-align: center;
    color: var(--headline-ink);
    font-weight: 800;
    font-size: 156px;
    line-height: 1;
    letter-spacing: -2px;
  }
  .headline--for { top: 59px; }
  .headline--lease { top: 244px; }
  .company-name {
    position: absolute;
    left: 0;
    top: 594px;
    width: 100%;
    margin: 0;
    text-align: center;
    color: var(--signal-red);
    font-weight: 600;
    font-size: 46px;
    line-height: 1;
    letter-spacing: 1px;
  }
  .contact-phone {
    position: absolute;
    left: 0;
    top: 716px;
    width: 100%;
    margin: 0;
    text-align: center;
    color: var(--signal-red);
    font-weight: 500;
    font-size: 57px;
    line-height: 1;
  }
  .contact-name {
    position: absolute;
    left: 0;
    top: 785px;
    width: 100%;
    margin: 0;
    text-align: center;
    color: var(--ink-dark);
    font-weight: 500;
    font-size: 37px;
    line-height: 1;
  }
</style>
</head>
<body>
  <main class="canvas">
    <section class="lease-sign">
      <div class="headline-band">
        <h1 class="headline headline--for">FOR</h1>
        <p class="headline headline--lease">LEASE</p>
      </div>
      <p class="company-name">Tall Oak RP, LLC</p>
      <p class="contact-phone">555-283-7716</p>
      <p class="contact-name">Reed Halvorsen</p>
    </section>
  </main>
</body>
</html>
```